Web Design for Small Healthcare Startup

Hello,

We are seeking a Website Design for a healthcare company focusing on mobile vaccinations, employee health and wellness services onsite at businesses, and consulting services relating to Healthcare Entities in WA state. Our company’s mission is to “To aid in a healthier workplace”. Brightpath Rovers will provide on-site wellness services to employers that simplify and streamline employee preventative health as well as onsite consulting services to help with compliance of Healthcare Entities.

We are seeking a Website Design for Brightpath Rovers, PLLC. Our company’s mission is to provide mobile health and wellness services to employers onsite at their businesses. These services include mobile vaccinations clinics for employees as well as wellness and health screenings. The company will also offer healtcare compliance consulting services for Healthcare Entities. The company was founded to bring these important healthcare services to businesses and keep employees healthy. Healthy employees are the cornerstone to a great business and we want to help orginazations achieve their goals of having a healthy productive workforce.

We are looking for a moderin website design that will need to be coded. We have attached our current logo design for reference as well as a brief questionare regarding our business for your information (not necessary to include all information). We would like something SEO friendly and easy to navigate.

Thank you!

Brightpath Rovers, PLLC

Target Market(s)

Small Businesses

Industry/Entity Type

Healthcare

Coding

Coded - Design and coding required

Number of Pages Required

1 page

Requirements
Nice to have
• SEO Friendly, Incorporate Logo

```html
<!DOCTYPE html>
<html lang="en">
<head>
<meta charset="utf-8">
<title>Brightpath Rovers, PLLC – On-site Mobile Vaccine Clinics</title>
<meta name="description" content="Brightpath Rovers provides seamless, hassle-free, on-site mobile vaccine clinics for workplaces.">
<link rel="stylesheet" href="https://fonts.googleapis.com/css2?family=Noto+Serif:wght@400&family=Open+Sans:wght@400;600&display=swap">
<style>
:root{
  --navy:#1b2a47;
  --blue:#0f57a8;
  --blue-field:#3f7cc1;
  --purple:#a2468f;
  --pink:#f6ebf3;
  --ink:#4a4a4a;
  --grey-card:#f4f4f4;
  --dark:#555555;
  --darker:#454545;
  --white:#ffffff;
}
*{box-sizing:border-box;margin:0;padding:0}
html,body{width:1200px;height:2627px;overflow:hidden}
body{position:relative;background:var(--white);font-family:"Open Sans",Arial,sans-serif;color:var(--ink)}
.abs{position:absolute}
.serif{font-family:"Noto Serif",Georgia,serif;font-weight:400}
a{color:inherit;text-decoration:none}

.topbar{left:0;top:0;width:1200px;height:31px;background:var(--navy);color:var(--white);font-size:11px}
.topbar .owner{position:absolute;left:160px;top:8px}
.topbar .top-contact{position:absolute;right:160px;top:8px;display:flex;gap:18px;align-items:center}
.topbar .top-contact span{display:flex;gap:5px;align-items:center}

.brand{left:192px;top:100px;font-size:26px;line-height:32px;color:var(--blue)}
.brand-mark{left:158px;top:104px;width:24px;height:24px;border-radius:50%;background:var(--purple)}
.nav{right:160px;top:48px;display:flex;gap:20px;font-size:12px;color:#555}
.nav a{padding-top:4px}
.nav a.active{border-top:2px solid var(--navy)}

.dots{background-image:radial-gradient(#c9ccd6 1.2px,transparent 1.4px);background-size:15px 15px}
.blur{border-radius:50%;filter:blur(22px)}

.hero-title{left:159px;top:230px;font-size:32px;line-height:37px;color:var(--blue);white-space:nowrap}
.hero-title em{font-style:normal;color:var(--purple)}
.hero-title .under{border-bottom:4px solid var(--blue)}
.hero-lead{left:158px;top:320px;width:300px;font-size:12px;line-height:14px}
.btn{display:inline-block;background:var(--blue);color:var(--white);font-size:12px;border-radius:20px;padding:10px 21px}
.hero-btn{left:159px;top:372px}
.hero-photo{left:548px;top:90px;width:420px;height:387px;border-radius:50%;background:radial-gradient(circle at 45% 40%,#f1e6e2 0%,#d8dde6 45%,#b8c6d8 75%,#e9eef5 100%)}
.hero-frame{left:690px;top:130px;width:280px;height:280px;border:4px solid var(--blue);border-radius:70px;transform:rotate(45deg)}

.pill{left:312px;top:541px;width:576px;height:212px;border-radius:106px;background:var(--blue);color:var(--white);text-align:center}
.pill .features{position:absolute;left:0;top:34px;width:100%;display:flex;justify-content:center}
.pill .feature{width:140px;font-size:11px}
.pill .feature svg{display:block;margin:0 auto 10px}
.pill .sep{width:1px;height:52px;background:var(--white);margin-top:2px}
.pill .tag{position:absolute;left:0;top:130px;width:100%;font-size:15px;line-height:23px}

.pink-block{border-radius:42px;background:var(--pink)}
.photo{border-radius:42px}
.flu-photo{left:159px;top:827px;width:431px;height:312px;background:linear-gradient(135deg,#e6e7ea 0%,#cfd2d8 40%,#d9b49a 70%,#eceae8 100%)}
.h2{font-size:24px;line-height:29px;color:var(--purple)}
.copy{font-size:12px;line-height:16px}
.flu-title{left:610px;top:905px}
.flu-copy{left:610px;top:950px;width:425px}
.flu-btn{left:610px;top:1022px}

.res-title{left:159px;top:1253px;width:420px}
.res-copy{left:159px;top:1327px;width:425px}
.res-btn{left:160px;top:1400px}
.test-photo{left:610px;top:1190px;width:431px;height:311px;background:linear-gradient(120deg,#8aa2bf 0%,#2f5fb8 40%,#c24640 75%,#2c2c34 100%)}

.sched-title{left:160px;top:1600px;font-size:24px;line-height:29px;color:var(--purple)}
.sched-btn{left:159px;top:1711px}
.step{top:1579px;width:207px;height:192px;border-radius:24px;background:var(--grey-card);border:1px solid #ddd;text-align:center;font-size:14px;line-height:19px;color:#555}
.step .num{width:78px;height:78px;margin:24px auto 18px;border-radius:50%;border:2px solid var(--blue);background:var(--white);font-family:"Noto Serif",Georgia,serif;font-size:44px;line-height:74px;color:#333}
.step.active{background:var(--dark);color:var(--white);border-color:var(--dark)}
.step.active .num{border-color:var(--purple)}

.contact-panel{left:0;top:1826px;width:600px;height:564px;background:var(--blue);color:var(--white)}
.contact-panel h3{position:absolute;left:160px;top:82px;font-size:16px;font-weight:400}
.field{position:absolute;height:33px;background:var(--blue-field);font-size:11px;padding:10px 13px;color:#eaf0f8}
.send{position:absolute;left:163px;top:300px;background:var(--white);color:#333;font-size:11px;padding:11px 16px}
.info{position:absolute;left:160px;font-size:11px;display:flex;gap:6px;align-items:center}
.map{left:600px;top:1826px;width:600px;height:564px;background:linear-gradient(160deg,#eef0f2 0%,#e6e9ec 50%,#dfe8f0 100%)}

.footer{left:0;top:2390px;width:1200px;height:202px;background:var(--dark);color:var(--white)}
.footer h4{position:absolute;top:53px;font-size:18px}
.footer .about{position:absolute;left:158px;top:92px;width:280px;font-size:11px;line-height:14px}
.footer ul{position:absolute;top:90px;list-style:none;font-size:11px;line-height:19px}
.subscribe{position:absolute;left:759px;top:86px;display:flex}
.subscribe span{display:block;width:184px;height:33px;background:var(--white);color:#666;font-size:11px;padding:10px 11px;border-radius:3px 0 0 3px}
.subscribe b{display:block;height:33px;background:var(--darker);font-weight:400;font-size:11px;padding:10px 11px;border-radius:0 3px 3px 0}
.social{position:absolute;left:760px;top:145px;display:flex;gap:18px}
.social i{display:block;width:14px;height:14px;background:var(--white);border-radius:2px}
.bottom{left:0;top:2592px;width:1200px;height:35px;background:var(--darker);color:#ddd;font-size:9px;padding:12px 160px}
</style>
</head>
<body>

<header>
  <div class="abs topbar">
    <span class="owner">Corinne Dalby, PharmD (Owner/Pharmacist)</span>
    <div class="top-contact">
      <span><svg width="9" height="9" viewBox="0 0 24 24"><path fill="#fff" d="M6.6 10.8a15 15 0 006.6 6.6l2.2-2.2c.3-.3.7-.4 1-.2 1.1.4 2.3.6 3.6.6.6 0 1 .4 1 1V20c0 .6-.4 1-1 1A17 17 0 013 4c0-.6.4-1 1-1h3.5c.6 0 1 .4 1 1 0 1.3.2 2.5.6 3.6.1.3 0 .7-.2 1z"/></svg>509-555-0142</span>
      <span><svg width="10" height="8" viewBox="0 0 20 16"><rect width="20" height="16" rx="2" fill="#fff"/><path d="M1 2l9 7 9-7" stroke="#1b2a47" stroke-width="2" fill="none"/></svg>cdalby@inboxmail.example</span>
    </div>
  </div>
  <div class="abs brand-mark"></div>
  <div class="abs brand serif">Brightpath Rovers</div>
  <nav class="abs nav">
    <a class="active" href="#">Home</a><a href="#">About</a><a href="#">Services</a><a href="#">Schedule Today</a><a href="#">Pricing</a>
  </nav>
</header>

<main>
  <div class="abs dots" style="left:108px;top:220px;width:120px;height:120px"></div>
  <div class="abs dots" style="left:445px;top:400px;width:120px;height:115px"></div>
  <h1 class="abs hero-title serif">Making the <em>workplace</em><br>A <em class="under">healthier</em> place</h1>
  <p class="abs hero-lead">Brightpath Rovers specializes in providing seamless, hassle-free, on-site mobile vaccine clinics</p>
  <a class="abs btn hero-btn" href="#">Get Vaccination Details</a>
  <div class="abs hero-frame"></div>
  <div class="abs hero-photo" role="img" aria-label="Pharmacist in a white coat holding a stethoscope in a bright office"></div>

  <section class="abs pill">
    <div class="features">
      <div class="feature">
        <svg width="50" height="52" viewBox="0 0 50 52" fill="none" stroke="#fff" stroke-width="2"><circle cx="13" cy="22" r="5"/><circle cx="25" cy="18" r="5"/><circle cx="37" cy="22" r="5"/><path d="M5 50V36a8 8 0 0116 0v14M17 50V32a8 8 0 0116 0v18M29 50V36a8 8 0 0116 0v14"/></svg>
        No crowded waiting rooms
      </div>
      <div class="sep"></div>
      <div class="feature">
        <svg width="50" height="52" viewBox="0 0 50 52" fill="none" stroke="#fff" stroke-width="2"><circle cx="10" cy="10" r="5"/><circle cx="25" cy="10" r="5"/><circle cx="40" cy="10" r="5"/><path d="M4 50V22h12v28M19 50V22h12v28M34 50V22h12v28"/></svg>
        No long lines
      </div>
      <div class="sep"></div>
      <div class="feature">
        <svg width="52" height="52" viewBox="0 0 52 52" fill="none" stroke="#fff" stroke-width="2"><circle cx="26" cy="26" r="24"/><circle cx="26" cy="26" r="12"/><path d="M20 26l4 4 8-8"/></svg>
        No hassle!
      </div>
    </div>
    <p class="tag">Specializing in workplace employee vaccine clinics. Great<br>service to offer as part of your company’s Employee</p>
  </section>
  <div class="abs blur" style="left:800px;top:740px;width:80px;height:70px;background:#9a9a9a"></div>
  <div class="abs blur" style="left:1085px;top:800px;width:100px;height:100px;background:#7ea6dc"></div>

  <section>
    <div class="abs pink-block" style="left:135px;top:803px;width:431px;height:310px"></div>
    <div class="abs photo flu-photo" role="img" aria-label="Gloved hands giving a vaccine injection into an upper arm"></div>
    <div class="abs dots" style="left:592px;top:870px;width:50px;height:60px"></div>
    <div class="abs dots" style="left:925px;top:960px;width:120px;height:115px"></div>
    <h2 class="abs h2 serif flu-title">Offering Flu &amp; Covid Vaccinations</h2>
    <p class="abs copy flu-copy">Lorem ipsum dolor sit amet, consectetur adipiscing elit, sed do eiusmod tempor incididunt ut labore et dolore magna aliqua. Quis ipsum suspendisse ultrices gravida. Risus commodo viverra maecenas.</p>
    <a class="abs btn flu-btn" href="#">Book Your Appointment Now</a>
  </section>
  <div class="abs blur" style="left:720px;top:1130px;width:80px;height:70px;background:#e3aee0"></div>

  <section>
    <div class="abs dots" style="left:104px;top:1320px;width:60px;height:120px"></div>
    <div class="abs dots" style="left:540px;top:1260px;width:70px;height:115px"></div>
    <h2 class="abs h2 serif res-title">Reserve your on-site mobile vaccine clinic today!</h2>
    <p class="abs copy res-copy">Lorem ipsum dolor sit amet, consectetur adipiscing elit, sed do eiusmod tempor incididunt ut labore et dolore magna aliqua. Quis ipsum suspendisse ultrices gravida. Risus commodo viverra maecenas.</p>
    <a class="abs btn res-btn" href="#">Book Your Appointment Now</a>
    <div class="abs pink-block" style="left:635px;top:1215px;width:431px;height:311px"></div>
    <div class="abs photo test-photo" role="img" aria-label="Health worker in protective gear swabbing a driver through a car window"></div>
  </section>
  <div class="abs blur" style="left:50px;top:1500px;width:80px;height:80px;background:#b0b0b0"></div>
  <div class="abs blur" style="left:320px;top:1450px;width:70px;height:60px;background:#c7d6ee"></div>

  <section>
    <div class="abs dots" style="left:104px;top:1605px;width:110px;height:120px"></div>
    <h2 class="abs sched-title serif">Schedule Your<br>Vaccination<br>Today</h2>
    <a class="abs btn sched-btn" href="#">Pricing Details</a>
    <div class="abs step" style="left:385px"><div class="num">1</div>Submit Vaccine Clinic<br>Needs Questionnaire.</div>
    <div class="abs step" style="left:609px"><div class="num">2</div>Brightpath Rovers, PLLC will<br>contact you to schedule<br>on-site vaccine clinic.</div>
    <div class="abs step active" style="left:834px"><div class="num">3</div>Prepare your employees<br>for vaccine clinic day.</div>
  </section>
  <div class="abs blur" style="left:360px;top:1730px;width:60px;height:60px;background:#efc6e8"></div>

  <section class="abs contact-panel">
    <h3>Corinne Dalby, PharmD (Owner/Pharmacist)</h3>
    <div class="field" style="left:160px;top:128px;width:193px">Enter Name</div>
    <div class="field" style="left:386px;top:128px;width:187px">Enter Email</div>
    <div class="field" style="left:160px;top:174px;width:193px">Enter Contact Number</div>
    <div class="field" style="left:386px;top:174px;width:187px">Location</div>
    <div class="field" style="left:160px;top:220px;width:413px;height:62px">Inquiring About ...</div>
    <div class="send">Send Query</div>
    <div class="info" style="top:366px"><svg width="11" height="11" viewBox="0 0 24 24"><path fill="none" stroke="#fff" stroke-width="2" d="M6.6 10.8a15 15 0 006.6 6.6l2.2-2.2 4.6 1.2V20A17 17 0 014 3h3.6l1 4.6z"/></svg>509-555-0142</div>
    <div class="info" style="top:396px"><svg width="12" height="10" viewBox="0 0 20 16"><rect x="1" y="1" width="18" height="14" fill="none" stroke="#fff" stroke-width="2"/><path d="M1 2l9 7 9-7" stroke="#fff" stroke-width="2" fill="none"/></svg>For Information: cdalby@inboxmail.example</div>
    <div class="info" style="top:415px"><svg width="11" height="11" viewBox="0 0 20 20"><rect x="2" y="2" width="16" height="16" fill="none" stroke="#fff" stroke-width="2"/></svg>For Query: help@brightpathrovers.example</div>
    <div class="info" style="top:434px"><svg width="11" height="11" viewBox="0 0 20 20" fill="none" stroke="#fff" stroke-width="2"><circle cx="10" cy="6" r="4"/><path d="M2 19a8 8 0 0116 0"/></svg>For Career: career@brightpathrovers.example</div>
    <div class="info" style="top:465px"><svg width="12" height="10" viewBox="0 0 22 18"><rect x="1" y="1" width="20" height="16" fill="none" stroke="#fff" stroke-width="2"/></svg>123, ABCD, Lorem Ipsum, Dolor Road, Pin - 12345</div>
  </section>
  <div class="abs map" role="img" aria-label="Street map showing the business location and surrounding roads and rivers"></div>
</main>

<footer>
  <div class="abs footer">
    <h4 class="serif" style="left:160px">Brightpath Rovers PLLC</h4>
    <p class="about">Lorem ipsum dolor sit amet, consectetur adipiscing elit, sed do eiusmod tempor incididunt ut labore et dolore magna aliqua. Quis ipsum suspendisse ultrices gravida.</p>
    <h4 class="serif" style="left:458px">Quick Links</h4>
    <ul style="left:458px"><li>Home</li><li>About</li><li>Services</li><li>Schedule Today</li></ul>
    <ul style="left:608px"><li>Contact</li><li>Pricing</li><li>Privacy Policy</li><li>Terms &amp; Condition</li></ul>
    <h4 class="serif" style="left:758px">Social &amp; Subscription</h4>
    <div class="subscribe"><span>Enter Your Email Here</span><b>Subscribe Now</b></div>
    <div class="social"><i></i><i></i><i></i><i></i><i></i></div>
  </div>
  <div class="abs bottom">Copyright reserved by © Brightpath Rovers PLLC. 2022</div>
</footer>

</body>
</html>
```